Companybrochure for Consulting & Financing Firm

I need to have a Company Brochure asap for our company. We have a website that describes what we do, but we need also a brochure, that can be sent by PDF of eventually be printed as well.

The brochure should be short but nice and appealing to the customers.

We provide professional management consulting and help our customers to get finance for very diferent projects. Our business has a lot to do with personal relations, but also we are very professional in the way we work and how develop the solutions for our clients. Our clients are mainly government-owned firm, but also private trading companies and wealthy private investors.

Our customers are mainly in Latin America, but the company is headquater is in Switzerland. We are opening offices in Panama and Caracas, this should be easaly be adabtable later.

Please have a look at our website www.valtorhaus.ch. In the brochure, we would segment our services in 1.) Project Developments 2.) Management Conulting 3.) Investment Management and 4.) Finance Solutions.

Also do have a look at www.valtorhaus.ch
(Click E for the English version)
Updates

I managed to put the Mock-Up to the Website.
It is actually not really a mock-up, it is a version I have designed myself.
Well as I am not a designer, I hope you can make it much better.
The content however is what I would put in any other design as well.

Target Market(s)

Top Management, Investors, Entrepreneurs, Government Officials

Industry/Entity Type

Management Consulting

Requirements
Must have
• Design should reflect this image elements:

We are entrepreneurs.
We are comitted to get things done.
We work closely with the client side by side.
We are a professional partner.
We are not afraid of delivering unconventional solutions.
We look at the problem from various angles.
We analyse, develop solutions and implent results.
Should not have
• Typical US-American style elements. We do not want to give the impression of being a US company.

We do not want to appear to be neo-liberal. We are a politically neutral professional consulting firm.

```html
<!DOCTYPE html>
<html lang="en">
<head>
<meta charset="utf-8">
<title>Valtorhaus AG – Finance Solutions</title>
<link rel="stylesheet" href="https://fonts.googleapis.com/css2?family=Arimo:wght@400;700&family=Open+Sans:wght@600;700&display=swap">
<style>
  :root {
    --canvas: #c4c5c7;
    --panel-grey: #d0d1d3;
    --heading-band: #e7e8ea;
    --navy-band: #3e5080;
    --brand-navy: #37468a;
    --body-grey: #77787b;
    --contact-blue: #5a60a4;
    --water-light: #bfe6ef;
    --water-mid: #7cc6da;
    --water-deep: #4aa3c2;
    --blue-glow: #1c93dc;
    --blue-mid: #2a6fb8;
    --blue-edge: #2c4687;
    --white: #ffffff;
  }
  * { box-sizing: border-box; margin: 0; padding: 0; }
  html, body { width: 1200px; height: 434px; overflow: hidden; }
  body {
    background: var(--canvas);
    font-family: "Arimo", Arial, sans-serif;
    position: relative;
  }
  .panel {
    position: absolute;
    top: 12px;
    width: 578px;
    height: 409px;
    background: var(--panel-grey);
    overflow: hidden;
  }
  .panel--service { left: 17px; }
  .panel--profile { left: 605px; }

  /* Left panel */
  .hero-photo {
    position: absolute; left: 0; top: 0; width: 578px; height: 210px;
    background: linear-gradient(180deg, var(--water-light) 0%, var(--water-mid) 60%, var(--water-deep) 100%);
  }
  .navy-band {
    position: absolute; left: 0; top: 210px; width: 578px; height: 12px;
    background: var(--navy-band);
  }
  .heading-band {
    position: absolute; left: 0; top: 222px; width: 578px; height: 42px;
    background: var(--heading-band);
  }
  .service-title {
    position: absolute; left: 51px; top: 228px;
    font-size: 26px; font-weight: 700; color: var(--brand-navy);
    letter-spacing: 0.1px;
  }
  .service-copy {
    position: absolute; left: 51px; top: 272px; width: 510px;
    font-size: 10.6px; line-height: 13px; color: var(--body-grey);
  }
  .service-copy p { margin-bottom: 13px; }

  /* Right panel */
  .values-block {
    position: absolute; left: 0; top: 0; width: 578px; height: 281px;
    background: radial-gradient(ellipse 330px 230px at 168px 120px, var(--blue-glow) 0%, var(--blue-mid) 45%, var(--blue-edge) 100%);
    color: var(--white);
  }
  .motto {
    position: absolute; left: 48px; top: 108px;
    font-size: 18.5px; font-weight: 700;
  }
  .values-list {
    position: absolute; left: 48px; top: 149px;
    list-style: none;
    font-family: "Open Sans", Calibri, sans-serif;
    font-size: 10.4px; font-weight: 700; line-height: 15.6px;
  }
  .registration {
    position: absolute; left: 48px; top: 302px;
    font-size: 12.2px; color: var(--brand-navy);
  }
  .contact {
    position: absolute; left: 48px; top: 335px;
    font-size: 10.6px; line-height: 11.6px; color: var(--contact-blue);
    font-style: normal;
  }
</style>
</head>
<body>
  <section class="panel panel--service">
    <div class="hero-photo" role="img" aria-label="Photo of two tropical fish leaping between glass fish bowls filled with water"></div>
    <div class="navy-band"></div>
    <div class="heading-band"></div>
    <h1 class="service-title">&gt;&gt; Finance Solutions</h1>
    <div class="service-copy">
      <p>Financing growth opportunities sometimes calls for an entrepreneurial perspective, which is often not found in the traditional banking world.</p>
      <p>That is why we have committed ourselves to developing financing solutions for unconventional requirements. To do so, we often work with partners with complementary subject matter expertise and geographical coverage.</p>
      <p>This gives us the flexibility to create innovative solutions – solutions that meet our clients’ special needs.</p>
    </div>
  </section>

  <section class="panel panel--profile">
    <div class="values-block">
      <h2 class="motto">&gt; Analyze &gt;&gt; Develop &gt;&gt;&gt; Deliver</h2>
      <ul class="values-list">
        <li>We are entrepreneurs.</li>
        <li>&gt; We are committed to get things done.</li>
        <li>&gt; We work closely with the client side by side.</li>
        <li>&gt; We apply structured methods of reasoning.</li>
        <li>&gt; We look at the problem from various angles.</li>
        <li>&gt; We are not afraid of delivering unconventional solutions.</li>
        <li>&gt; We analyze situations, develop solutions and implement results.</li>
      </ul>
    </div>
    <p class="registration">Valtorhaus AG is registered as a Swiss stock corporation since 1995.</p>
    <address class="contact">
      Valtorhaus AG<br>
      Lindenhof-Strasse 14, CH-8001 Zürich<br>
      Tel. +41 44 512 30 40 | Fax. +41 44 512 30 49<br>
      www.valtorhaus.ch | info@valtorhaus.ch
    </address>
  </section>
</body>
</html>
```